Larkspur Realty

Business cards for 4 people

They need to say for all
57 Danner Quay, Boston MA 02117

Each person will have their own personal information
We would like gold embossing for the name of the company
Mabel is the blonde sitting in the chair smiling her information should be on the back of the card with her name and information
Should say for slogan classic pattern, elevated experience
mabel@larkspurhomesnet.com
(413) 555-0182

Odessa is the brunette with wavy hair in the tan suit odessa@larkspurhomesnet.com
(617) 555-0147

june@larkspurhomesnet.com
(413) 555-0169
standing next to the chair

ruth@larkspurhomesnet.com
(413) 555-0193
close up headshot

```html
<!DOCTYPE html>
<html lang="en">
<head>
<meta charset="utf-8">
<title>Larkspur Realty – Business Cards</title>
<link rel="stylesheet" href="https://fonts.googleapis.com/css2?family=Poppins:wght@400;600&display=swap">
<style>
  :root {
    --backdrop: #c4c6c9;
    --navy-deep: #173a5c;
    --navy-mid: #1f466c;
    --navy-light: #3a6186;
    --gold: #f2c53d;
    --ink-light: #f3f5f8;
    --photo-warm: #8a6a4e;
    --photo-dark: #5a4334;
  }
  * { box-sizing: border-box; margin: 0; padding: 0; }
  html, body { width: 1200px; height: 781px; overflow: hidden; }
  body {
    background: var(--backdrop);
    font-family: "Poppins", sans-serif;
    position: relative;
  }
  .card {
    position: absolute;
    border-radius: 18px;
    background: linear-gradient(160deg, var(--navy-mid) 0%, var(--navy-deep) 55%, var(--navy-light) 100%);
    box-shadow: 0 10px 24px rgba(0,0,0,0.22);
    overflow: hidden;
  }
  /* Personal side */
  .card-personal {
    left: 150px; top: 136px;
    width: 292px; height: 510px;
  }
  .portrait {
    position: absolute;
    left: 70px; top: 48px;
    width: 170px; height: 270px;
    border-radius: 80px 80px 10px 10px;
    background: linear-gradient(180deg, var(--photo-warm) 0%, var(--photo-dark) 55%, rgba(31,70,108,0) 100%);
    opacity: 0.85;
  }
  .details {
    position: absolute;
    left: 34px; top: 310px;
    color: var(--ink-light);
    font-size: 13px;
    line-height: 1.55;
  }
  .person-name {
    color: var(--gold);
    font-weight: 600;
    font-size: 22px;
    line-height: 1.2;
  }
  .slogan { margin-bottom: 10px; }
  .address { margin-bottom: 8px; }
  .contact-line { display: flex; align-items: center; gap: 7px; }
  .contact-line svg { width: 11px; height: 11px; fill: var(--gold); flex: none; }
  /* Brand side */
  .card-brand {
    left: 560px; top: 246px;
    width: 510px; height: 292px;
    display: flex; align-items: center; justify-content: center; gap: 18px;
  }
  .brand-name {
    color: var(--gold);
    font-weight: 600;
    font-size: 36px;
    letter-spacing: 1px;
  }
  .brand-mark {
    width: 46px; height: 46px;
    border-radius: 50%;
    border: 3px solid var(--gold);
  }
</style>
</head>
<body>
  <section class="card card-personal">
    <div class="portrait" role="img" aria-label="Photo of Odessa seated on a wooden chair in a tan suit"></div>
    <div class="details">
      <p class="person-name">Odessa Marchand</p>
      <p class="slogan">Elevated Experience</p>
      <p class="address">57 Danner Quay,<br>Boston MA 02117</p>
      <p class="contact-line">
        <svg viewBox="0 0 24 24" aria-hidden="true"><path d="M6.6 10.8a15 15 0 0 0 6.6 6.6l2.2-2.2a1 1 0 0 1 1-.25 11.4 11.4 0 0 0 3.6.57 1 1 0 0 1 1 1V20a1 1 0 0 1-1 1A17 17 0 0 1 3 4a1 1 0 0 1 1-1h3.5a1 1 0 0 1 1 1c0 1.25.2 2.45.57 3.57a1 1 0 0 1-.25 1z"/></svg>
        (617) 555-0147
      </p>
      <p class="contact-line">
        <svg viewBox="0 0 24 24" aria-hidden="true"><path d="M2 5h20v14H2z M4 7v.5l8 5 8-5V7l-8 5z" fill-rule="evenodd"/></svg>
        odessa@larkspurhomesnet.com
      </p>
      <p class="contact-line">
        <svg viewBox="0 0 24 24" aria-hidden="true"><circle cx="12" cy="12" r="10"/></svg>
        www.larkspurhomesnet.com
      </p>
    </div>
  </section>

  <section class="card card-brand">
    <span class="brand-name">Larkspur Realty</span>
    <span class="brand-mark" aria-hidden="true"></span>
  </section>
</body>
</html>
```